Brightwater Leadership Workshop

I need a powerpoint template with a cover design and 5-6 slide designs for content. The graphic I'd like to use is a speech or thought bubble. I'd like it to look classy, not cartoonish. Shades of blue - not pastel or neon

```html
<!DOCTYPE html>
<html lang="en">
<head>
<meta charset="utf-8">
<title>Brightwater Leadership Workshop – Cover</title>
<link rel="stylesheet" href="https://fonts.googleapis.com/css2?family=Carlito:wght@400;700&display=swap">
<style>
  :root {
    --sky-light: #cdd9e6;
    --sky-mid: #7f9ab8;
    --tower-dark: #0b1626;
    --tower-mid: #1c3150;
    --warm-glow: #5a3a1c;
    --bubble-top: #2c5cb0;
    --bubble-bottom: #0f2a58;
    --text-light: #ffffff;
  }
  * { margin: 0; padding: 0; box-sizing: border-box; }
  html, body { width: 1200px; height: 667px; overflow: hidden; background: var(--tower-dark); }
  .cover {
    position: relative;
    width: 1200px;
    height: 667px;
    overflow: hidden;
    font-family: "Carlito", "Calibri", sans-serif;
    color: var(--text-light);
  }
  .cover__photo {
    position: absolute;
    inset: 0;
    background:
      radial-gradient(ellipse 260px 340px at 930px 360px, var(--sky-light) 0%, rgba(205,217,230,0.6) 45%, rgba(205,217,230,0) 100%),
      radial-gradient(ellipse 300px 120px at 560px 640px, rgba(90,58,28,0.9) 0%, rgba(90,58,28,0) 100%),
      linear-gradient(160deg, var(--tower-mid) 0%, var(--sky-mid) 55%, var(--tower-dark) 100%);
  }
  .cover__bubble {
    position: absolute;
    left: 0;
    top: 0;
    width: 1200px;
    height: 667px;
  }
  .cover__content {
    position: absolute;
    left: 106px;
    top: 122px;
  }
  .cover__title {
    font-size: 42px;
    font-weight: 700;
    line-height: 47px;
    letter-spacing: 0.2px;
  }
  .cover__subtitle {
    margin-top: 54px;
    font-size: 18px;
    font-weight: 400;
  }
  .cover__presenter {
    margin-top: 52px;
    font-size: 21px;
    font-weight: 700;
  }
</style>
</head>
<body>
  <main class="cover">
    <div class="cover__photo" role="img" aria-label="Upward view of glass office skyscrapers against a pale sky"></div>

    <svg class="cover__bubble" viewBox="0 0 1200 667" aria-hidden="true">
      <defs>
        <linearGradient id="bubbleFill" x1="0" y1="0" x2="0" y2="1">
          <stop offset="0" stop-color="var(--bubble-top)"/>
          <stop offset="1" stop-color="var(--bubble-bottom)"/>
        </linearGradient>
      </defs>
      <path d="M0 0 L921 0 C915 120 815 225 661 314 C560 370 440 497 261 497 C140 497 50 445 0 391 Z"
            fill="url(#bubbleFill)" opacity="0.9"/>
    </svg>

    <section class="cover__content">
      <h1 class="cover__title">Brightwater Leadership<br>Workshop</h1>
      <p class="cover__subtitle">Business Presentation Deck</p>
      <p class="cover__presenter">Mr. Daniel Marsh</p>
    </section>
  </main>
</body>
</html>
```